Bref créative
Business Card for "Homeward by Plan"
Business card for senior move management company
Simple
Dalia Fenwick
Owner / CEO
Cedar Ridge, OH
dalia@homeplanex.com
www.homeplanex.com
Relocation | Organizing | Interior Design
Attached is the file for the homeward by plan business cards
png logo file for homewrd by plan
jpeg for homeward by plan business cards

```html
<!DOCTYPE html>
<html lang="en">
<head>
<meta charset="utf-8">
<title>Homeward by Plan — Stationery</title>
<link rel="stylesheet" href="https://fonts.googleapis.com/css2?family=Cormorant+Garamond:wght@600&family=Lato:wght@400&display=swap">
<style>
  :root {
    --backdrop: #2a2a2b;
    --paper: #ffffff;
    --sage: #6e8767;
    --bark: #8a5b3a;
    --ink: #5a5a5a;
    --rule: #e4e4e4;
    --serif: "Cormorant Garamond", Georgia, serif;
    --sans: "Lato", Arial, sans-serif;
  }
  * { margin: 0; padding: 0; box-sizing: border-box; }
  html, body { width: 1200px; height: 845px; overflow: hidden; }
  body { background: var(--backdrop); position: relative; font-family: var(--sans); }

  .sheet { position: absolute; background: var(--paper); box-shadow: 0 3px 10px rgba(0,0,0,.45); }
  .card { border-radius: 10px; }

  .brand { display: flex; align-items: center; gap: 6px; white-space: nowrap; }
  .brand-dot { border-radius: 50%; background: var(--sage); flex: none; }
  .brand-name { font-family: var(--serif); font-weight: 600; color: var(--bark); line-height: 1.05; text-transform: uppercase; letter-spacing: .03em; }
  .centered { position: absolute; left: 0; right: 0; justify-content: center; }

  .tagline { font-size: 5px; letter-spacing: .03em; white-space: nowrap; }

  /* letterhead */
  .letterhead { left: 252px; top: 252px; width: 324px; height: 528px; }
  .letterhead .brand { top: 40px; }
  .letterhead .brand-dot { width: 24px; height: 24px; }
  .letterhead .brand-name { font-size: 13px; }
  .letterhead-footer { position: absolute; left: 0; right: 0; bottom: 18px; text-align: center; font-size: 6px; color: var(--ink); white-space: nowrap; }

  /* business card, white front */
  .card-front { left: 700px; top: 106px; width: 134px; height: 86px; }
  .card-front .brand { top: 24px; }
  .card-front .brand-dot { width: 14px; height: 14px; }
  .card-front .brand-name { font-size: 8px; }
  .card-front .tagline { position: absolute; left: 0; right: 0; bottom: 12px; text-align: center; color: var(--ink); font-size: 4px; }

  /* business card, green back */
  .card-green { left: 595px; top: 233px; width: 202px; height: 122px; background: var(--sage); }
  .card-green .panel { position: absolute; left: 10px; top: 12px; width: 182px; height: 80px; background: var(--paper); border-radius: 6px; }
  .card-green .brand { top: 40px; }
  .card-green .brand-dot { width: 18px; height: 18px; }
  .card-green .brand-name { font-size: 10px; }
  .card-green .tagline { position: absolute; left: 0; right: 0; bottom: 12px; text-align: center; color: var(--paper); }

  /* business card, contact */
  .card-contact { left: 811px; top: 233px; width: 195px; height: 122px; }
  .card-contact .brand { position: absolute; left: 14px; top: 46px; }
  .card-contact .brand-dot { width: 14px; height: 14px; }
  .card-contact .brand-name { font-size: 7px; }
  .contact { position: absolute; left: 92px; top: 28px; font-size: 5.5px; color: var(--ink); line-height: 1.55; }
  .contact .person { font-family: var(--serif); font-weight: 600; font-size: 10px; color: var(--bark); line-height: 1.2; }

  /* envelopes */
  .envelope { width: 413px; overflow: hidden; }
  .envelope .flap { position: absolute; left: 0; top: 0; }
  .envelope .flap-text { position: absolute; left: 0; right: 0; text-align: center; color: var(--paper); }

  .envelope-front { left: 595px; top: 365px; height: 211px; }
  .envelope-front .flap-text { top: 12px; transform: rotate(180deg); }
  .envelope-front .brand { position: absolute; left: 22px; top: 70px; }
  .envelope-front .brand-dot { width: 20px; height: 20px; }
  .envelope-front .brand-name { font-size: 11px; }
  .envelope-front .address { position: absolute; left: 48px; top: 94px; font-size: 6px; color: var(--ink); }

  .envelope-back { left: 595px; top: 595px; height: 185px; }
  .envelope-back .flap-text { top: 14px; }
</style>
</head>
<body>

  <section class="sheet letterhead">
    <div class="brand centered"><span class="brand-dot"></span><span class="brand-name">Homeward by Plan</span></div>
    <p class="letterhead-footer">Cedar Ridge, OH &nbsp;|&nbsp; p 555.201.0148 &nbsp;|&nbsp; dalia@homeplanex.com &nbsp;|&nbsp; homeplanex.com</p>
  </section>

  <section class="sheet card card-front">
    <div class="brand centered"><span class="brand-dot"></span><span class="brand-name">Homeward by Plan</span></div>
    <p class="tagline">Relocation | Organizing | Interior Design</p>
  </section>

  <section class="sheet card card-green">
    <div class="panel"></div>
    <div class="brand centered"><span class="brand-dot"></span><span class="brand-name">Homeward by Plan</span></div>
    <p class="tagline">Relocation | Organizing | Interior Design</p>
  </section>

  <section class="sheet card card-contact">
    <div class="brand"><span class="brand-dot"></span><span class="brand-name">Homeward<br>by Plan</span></div>
    <div class="contact">
      <p class="person">Dalia Fenwick</p>
      <p>Owner / CEO</p>
      <p>Cedar Ridge, OH</p>
      <p>p 555.201.0148</p>
      <p>dalia@homeplanex.com</p>
      <p>www.homeplanex.com</p>
    </div>
  </section>

  <section class="sheet envelope envelope-front">
    <svg class="flap" width="413" height="60" viewBox="0 0 413 60" aria-hidden="true">
      <path d="M0 0 H413 V30 Q413 40 400 42 Q206 62 13 42 Q0 40 0 30 Z" fill="var(--sage)"/>
    </svg>
    <p class="tagline flap-text">Relocation | Organizing | Interior Design</p>
    <div class="brand"><span class="brand-dot"></span><span class="brand-name">Homeward by Plan</span></div>
    <p class="address">Cedar Ridge, OH</p>
  </section>

  <section class="sheet envelope envelope-back">
    <svg class="flap" width="413" height="185" viewBox="0 0 413 185" aria-hidden="true">
      <path d="M0 0 H413 V28 Q413 36 400 38 Q206 60 13 38 Q0 36 0 28 Z" fill="var(--sage)"/>
      <path d="M0 185 L190 70 Q206 62 222 70 L413 185" fill="none" stroke="var(--rule)" stroke-width="1"/>
    </svg>
    <p class="tagline flap-text">Relocation | Organizing | Interior Design</p>
  </section>

</body>
</html>
```